Every Stage Theatre School Dance, drama & singing classes for ages 3-18yrs

Why pay of three classes when you can learn all three theatrical disciplines in one affordable, fantastically fun session? We are a nationally accredited school and offer the option of taking vocational exams with BRVEX & KOSP , as well as unparalleled performance opportunities both locally & in the Pellam Row. Our quality training is evident in our pupils success, through our TV & Theatrical agency current pupils have won major TV & stage roles with former pupils going on to become series regulars in Brackenfold & Kettle and lane. So whether it's a new hobby to build confidence, improve speech & language skills & make new friends, or with an eye to a professional career in performing arts, EST is leading the way in high quality classes at prices you can afford.

(possible bullet points:)
* After- school classes as well as our Saturday performers academy in Bexley, Bromley, Sidcup & the surrounds

* Classes are suited to various abilities from beginners to advanced in a fun & friendly environment

* Our ethos is to keep prices low making our training available to all

* Teachers are PVQ checked industry experts with nationally recognised teaching qualifications

* Our professional TV & Theatrical agency is available to all of our pupils.

Reason: I have extended the deadline in order for designers to have a bit longer to make changed etc or for any other submissions, though I would like to have a design within the next couple of days x

Target Market(s)

Parents and children & teenagers ages 3-18yrs

Industry/Entity Type

Performing Art

Requirements
Must have
• * Mention that we are up too 50% cheaper than other theatre schools AFFORDABLE
• * We are a nationally recognised accredited theatre school
• * We offer vocational exams with 100% pass rate
• * Our ethos is that every child should learn and build confidence and self-esteem through actual performing experience, therefor we offer unparalleled performance opportunities both locally & in the Pellam Row
• *We offer After-School classes as well as our Saturday Performers Academy
• * We have a professional TV and Film agency available to all of our pupils
• * Our quality training is evident in our pupils success ( See attached photos)
• * Teachers are PVQ checked industry professionals with nationally recognnised teaching qualifications.
• *VQRN logo ( attached)
• * FB page https://www.example-social.test/Everystagetheatre?fref=photo
• Photo's attached
• 1. Dorran- Major UK TV commercial
• 2. Tamsin - Playing the title role of Posy at The Marlow Playhouse
• 3. Reed - UK tour of 'The Lark in Winter'
• 4.Rosalind - London production of 'The Harbour Cousins'
• 4.Fergus- New TV series 'Class of Muddle'
• 5. Odette - Major American TV commercial
• 5. Morgan - Cpt Venn trailer NTK
• I have also attached some performance photos of our pupils if you need any
• Also attached is our old filer which was a little too wordy!!
Nice to have
• Mention of BRVEX drama exams and KOSP dance exams ( possibly use logos attached.

```html
<!DOCTYPE html>
<html lang="en">
<head>
<meta charset="utf-8">
<title>Every Stage Theatre School</title>
<link href="https://fonts.googleapis.com/css2?family=Open+Sans:wght@400;600;700;800&display=swap" rel="stylesheet">
<style>
:root{
  --ink:#1d1d1f;
  --night:#0d0d10;
  --night-soft:#2a2a30;
  --white:#ffffff;
  --pink:#e5127d;
  --yellow:#ffd200;
  --green:#6cbf2c;
  --grey:#555555;
}
*{margin:0;padding:0;box-sizing:border-box}
html,body{width:851px;height:1200px;overflow:hidden}
body{font-family:"Open Sans",Arial,sans-serif;background:var(--white);color:var(--ink)}
.flyer{position:relative;width:851px;height:1200px;overflow:hidden}
.dark-panel{position:absolute;left:0;top:0;width:851px;height:808px;
  background:radial-gradient(ellipse at 70% 55%,var(--night-soft) 0%,var(--night) 65%)}
.hero-photo{position:absolute;left:0;top:0;width:851px;height:250px;
  background:linear-gradient(180deg,#3b3b44 0%,#5b5c66 45%,#1b1b20 100%)}
.brand{position:absolute;left:24px;top:22px;display:flex;align-items:center;gap:10px;
  background:var(--night);padding:12px 16px;border-radius:6px}
.brand-dot{width:26px;height:26px;border-radius:50%;background:var(--pink)}
.brand-name{font-weight:800;font-size:23px;line-height:1.05;color:var(--pink)}
.facts{position:absolute;left:36px;top:272px;list-style:none;color:var(--white);font-size:14px;line-height:1.4}
.facts li{position:relative;padding-left:34px;margin-bottom:15px;font-weight:600}
.facts li.wide{width:770px}
.facts li.narrow{width:560px}
.facts li svg{position:absolute;left:0;top:-1px;width:22px;height:22px}
.hl-yellow{color:var(--yellow)}
.hl-green{color:var(--green)}
.offer{position:absolute;left:650px;top:520px;width:180px;height:140px;background:var(--white);
  border-radius:16px;padding:12px 10px;text-align:center}
.offer-title{font-size:21px;font-weight:800;color:var(--green)}
.offer-text{font-size:15px;font-weight:700;color:var(--pink);line-height:1.2;margin-top:4px}
.offer-text strong{font-size:24px;font-weight:800}
.success-title{position:absolute;left:0;top:828px;width:851px;text-align:center;
  font-size:22px;font-weight:700;color:var(--green)}
.pupils{position:absolute;left:22px;top:876px;display:flex;gap:12px;list-style:none}
.pupil{width:106px;text-align:center}
.pupil-photo{width:84px;height:84px;border-radius:50%;margin:0 auto 10px;
  background:linear-gradient(160deg,#c9b39f 0%,#8a7a6e 100%);border:3px solid #eee}
.pupil-caption{font-size:12px;line-height:1.3;color:var(--grey);font-weight:600}
.pupil-caption b{color:var(--pink);font-weight:800}
.contact{position:absolute;left:36px;top:1110px;font-size:15px;font-weight:600;color:var(--ink)}
.contact-row{display:flex;align-items:center;gap:10px;margin-bottom:12px}
.contact-row svg{width:22px;height:22px}
.contact-row .phone{margin-left:22px;display:flex;align-items:center;gap:8px}
.social-square{width:20px;height:20px;background:#3b5998;border-radius:3px}
.badges{position:absolute;right:30px;top:1108px;display:flex;gap:16px;align-items:center}
.badge{background:#1e2f6b}
.badge.one{width:78px;height:62px}
.badge.two{width:92px;height:62px;background:#c7173d}
.badge.three{width:110px;height:62px;background:#233e85}
</style>
</head>
<body>
<div class="flyer">
  <div class="dark-panel"></div>
  <div class="hero-photo" role="img" aria-label="Stage photograph of young performers in hats and costumes"></div>

  <div class="brand">
    <span class="brand-dot"></span>
    <span class="brand-name">Every Stage<br>Theatre School</span>
  </div>

  <ul class="facts">
    <li class="wide"><svg viewBox="0 0 24 24"><path fill="#ffd200" d="M12 1l3.3 7 7.7.9-5.7 5.2 1.6 7.6L12 17.9 5.1 21.7l1.6-7.6L1 8.9 8.7 8z"/></svg>We are a nationally recognised accredited theatre school offering high quality <span class="hl-yellow">drama, singing &amp; dance</span> sessions from ages 3-18yrs</li>
    <li class="wide"><svg viewBox="0 0 24 24"><path fill="#ffd200" d="M12 1l3.3 7 7.7.9-5.7 5.2 1.6 7.6L12 17.9 5.1 21.7l1.6-7.6L1 8.9 8.7 8z"/></svg>We offer vocational exams with <span class="hl-green">100% pass rate</span></li>
    <li class="wide"><svg viewBox="0 0 24 24"><path fill="#ffd200" d="M12 1l3.3 7 7.7.9-5.7 5.2 1.6 7.6L12 17.9 5.1 21.7l1.6-7.6L1 8.9 8.7 8z"/></svg>Classes are suited to various abilities from beginners to advanced in a fun &amp; friendly environment</li>
    <li class="wide"><svg viewBox="0 0 24 24"><path fill="#ffd200" d="M12 1l3.3 7 7.7.9-5.7 5.2 1.6 7.6L12 17.9 5.1 21.7l1.6-7.6L1 8.9 8.7 8z"/></svg>Our ethos is that every child should learn and build confidence and self-esteem through actual performing experience, therefore we offer unparalleled performance opportunities both locally &amp; in the Pellam Row</li>
    <li class="narrow"><svg viewBox="0 0 24 24"><path fill="#ffd200" d="M12 1l3.3 7 7.7.9-5.7 5.2 1.6 7.6L12 17.9 5.1 21.7l1.6-7.6L1 8.9 8.7 8z"/></svg>Teachers are PVQ checked industry professionals with nationally recognised teaching qualifications</li>
    <li class="narrow"><svg viewBox="0 0 24 24"><path fill="#ffd200" d="M12 1l3.3 7 7.7.9-5.7 5.2 1.6 7.6L12 17.9 5.1 21.7l1.6-7.6L1 8.9 8.7 8z"/></svg>We offer After-School classes as well as our Saturday Performers Academy in <span class="hl-yellow">Bexley, Bromley, Sidcup &amp; the surrounds</span></li>
    <li class="narrow"><svg viewBox="0 0 24 24"><path fill="#ffd200" d="M12 1l3.3 7 7.7.9-5.7 5.2 1.6 7.6L12 17.9 5.1 21.7l1.6-7.6L1 8.9 8.7 8z"/></svg>Our ethos is to keep prices low making our training available to all</li>
    <li class="narrow"><svg viewBox="0 0 24 24"><path fill="#ffd200" d="M12 1l3.3 7 7.7.9-5.7 5.2 1.6 7.6L12 17.9 5.1 21.7l1.6-7.6L1 8.9 8.7 8z"/></svg>Our hugely successful TV &amp; Theatrical agency is available to all of our pupils.</li>
    <li class="narrow"><svg viewBox="0 0 24 24"><path fill="#ffd200" d="M12 1l3.3 7 7.7.9-5.7 5.2 1.6 7.6L12 17.9 5.1 21.7l1.6-7.6L1 8.9 8.7 8z"/></svg>Our Award winning classes are now in their fantastic 14th year!</li>
  </ul>

  <div class="offer">
    <div class="offer-title">AFFORDABLE!</div>
    <div class="offer-text">we are up to <strong>50%</strong><br>cheaper than other theatre schools</div>
  </div>

  <h2 class="success-title">Our quality training is evident in our pupils success</h2>

  <ul class="pupils">
    <li class="pupil"><div class="pupil-photo" role="img" aria-label="Portrait photo of pupil Reed"></div><p class="pupil-caption"><b>Reed</b> UK tour of 'The Lark in Winter'</p></li>
    <li class="pupil"><div class="pupil-photo" role="img" aria-label="Portrait photo of pupil Odette"></div><p class="pupil-caption"><b>Odette</b> Major American TV commercial</p></li>
    <li class="pupil"><div class="pupil-photo" role="img" aria-label="Portrait photo of pupil Rosalind"></div><p class="pupil-caption"><b>Rosalind</b> London production of 'The Harbour Cousins'</p></li>
    <li class="pupil"><div class="pupil-photo" role="img" aria-label="Portrait photo of pupil Morgan"></div><p class="pupil-caption"><b>Morgan</b> Cpt Venn trailer NTK</p></li>
    <li class="pupil"><div class="pupil-photo" role="img" aria-label="Portrait photo of pupil Fergus"></div><p class="pupil-caption"><b>Fergus</b> New TV series 'Class of Muddle'</p></li>
    <li class="pupil"><div class="pupil-photo" role="img" aria-label="Portrait photo of pupil Dorran"></div><p class="pupil-caption"><b>Dorran</b> Major UK TV commercial</p></li>
    <li class="pupil"><div class="pupil-photo" role="img" aria-label="Portrait photo of pupil Tamsin"></div><p class="pupil-caption"><b>Tamsin</b> Playing the title role of Posy at The Marlow Playhouse</p></li>
  </ul>

  <div class="contact">
    <div class="contact-row">
      <svg viewBox="0 0 24 24"><circle cx="12" cy="12" r="10" fill="none" stroke="#e5127d" stroke-width="2"/><ellipse cx="12" cy="12" rx="4.5" ry="10" fill="none" stroke="#e5127d" stroke-width="2"/><path d="M2 12h20" stroke="#e5127d" stroke-width="2"/></svg>
      <span>www.everystage.test</span>
      <span class="phone"><svg viewBox="0 0 24 24"><path fill="#e5127d" d="M6.6 10.8a15 15 0 006.6 6.6l2.2-2.2a1 1 0 011-.25 11.4 11.4 0 003.6.57 1 1 0 011 1V20a1 1 0 01-1 1A17 17 0 013 4a1 1 0 011-1h3.5a1 1 0 011 1c0 1.25.2 2.45.57 3.57a1 1 0 01-.25 1z"/></svg>020 7946 0321</span>
    </div>
    <div class="contact-row">
      <span class="social-square"></span>
      <span>https://www.example-social.test/Everystagetheatre</span>
    </div>
  </div>

  <div class="badges">
    <span class="badge one" aria-label="KOSP exams badge"></span>
    <span class="badge two" aria-label="BRVEX exams badge"></span>
    <span class="badge three" aria-label="VQRN accreditation badge"></span>
  </div>
</div>
</body>
</html>
```